BrambleShore.com Web Site Theme - Home Page/Front Page - Sub-Page theme

Looking for a new site theme that uses tiles like Plinkerdaily.com but with a unique style. Topbar categories should include following in any particular order w/ pop-out at touch w/ sub-categories (examples below): The main categories for display have an >> prefix . Note main catgories and sub-categories may change.

SPECIAL NOTE: Regional site. We need a way to navigate/drill-down to specific regions on the Bramble Shore (see the cities accross the top on the current site design)

PORTAL SITE: This site will have a back-end w/ my account and therefore may use a Scaffolix template on the back-end for managing Tiles and articles. Tiles would be the organic content/advertisements on the home page that link to the sub-pages.

TOP BAR CATEGORIES - click to open pop-up w/ sub-categories (some examples in Dining and Real Estate below)

>>Lodging

>>Dining (sub categories below)
Go to Dining >>
Bars & Nightclubs
Lunch & Dinner
Catering
Chinese
Coffee
Italian
Pizza
Seafood
Steakhouse
More >>

>>Wineries

>>Activities & Events

>>Real Estate

>>For Sale (subcategories below)
Auto
Shopping

>>Jobs
..

Target Market(s)

Hotels, Wineries, Restaurants, Tourists

Industry/Entity Type

Real Estate

Coding

Coded - Design and coding required

Number of Pages Required

3 page

Colors
0255a3

Requirements
Must have
• My account (maybe a black bar w/ BS logo accross top w/ My Account, Settings, Login etc)
• Conversion of existing organic content and advertisements to new Tiles platform.
Nice to have
• Kind of a Hybrid between Zorv.com and PlinkerDaily.com
• PORTAL THOUGHTS
• If everything were to be thought of as a tile to preview in a 3 column wide format w/ variable heights you can fit articles and sound content mixed in with advertorials.
• Every square tile on BrambleShore.com could be encapsulated into a “Tile”. The Tile is the preview of the landing page, article, or page.
• Every article, business listings, google map page, etc. can have a Tile associated with it. OR you create a Tile and link it to a URL/page.
• So Tiles become mini snippets of custom HTML that can have 1 or more links etc… Just an HTML Snippet.
• Tile/HTML Snippet
• PreviewTiles.aspx
• Shows all tiles sortable like a product catalog, etc. Additional columns for publishing the tile and where it should reside on the Front Page?
• NEW THEME
• Removal of the traditional BS sidebar and incorporating the triple tile site design. We can still have Fernmarsh or a major display as first thing you see above top-bar. The categories can be incorporated into a simple top-bar that on-click you pop-down all subcategories and anything featured. This supports tablets and handhelds instead of the traditional mouse-over...
• Comp Layout (see plinkerdaily.com)
• 3 columns to 1 column style?
• How to handle mobile devices? (Tiles technique supports Quibbit news mobile app - 3 columns PC/Mac browser - 1 column Mobile Phone
• Tile & Page MGT
• How do we convert the existing content pages to our new Tile/Page technique?
• How do we handle advertising Tiles and Tiles embedded on pages?
• Pages
• How is a page handled?
• How are Tiles managed and is that a Page or not?
• How are listings handled and are they defined as a Page?

```html
<!DOCTYPE html>
<html lang="en">
<head>
<meta charset="utf-8">
<title>BrambleShore.com — Home</title>
<link href="https://fonts.googleapis.com/css2?family=Raleway:wght@400;500;600&family=Roboto:wght@400;500&display=swap" rel="stylesheet">
<style>
:root{
  --blue:#0255a3;
  --blue-dark:#0a3f80;
  --ink:#222;
  --muted:#777;
  --topbar:#111214;
  --header:#1d1f23;
  --footer:#1d1f23;
  --bottom:#141517;
  --strip:#e4e8ef;
  --panel:#dfe3ea;
  --line:#dcdfe4;
  --field:#2c2f34;
}
*{box-sizing:border-box;margin:0;padding:0}
html,body{width:668px;height:1200px;overflow:hidden}
body{position:relative;background:#fff;font-family:"Roboto",Arial,sans-serif;color:var(--ink)}
.abs{position:absolute}
.topbar{left:0;top:0;width:668px;height:20px;background:var(--topbar);font-size:5.6px;color:#ccc;letter-spacing:.3px}
.topbar ul{position:absolute;right:62px;top:6px;display:flex;gap:11px;list-style:none}
.topbar .call{color:#5b8fd0}
.topbar .call b{color:#aaa;font-weight:400}
.topbar li.sq::before{content:"";display:inline-block;width:2px;height:2px;background:var(--blue);margin:0 3px 1px 0}
.header{left:0;top:20px;width:668px;height:42px;background:var(--header)}
.brand{left:62px;top:10px;display:flex;align-items:center;gap:5px;font-family:"Raleway",sans-serif;font-weight:600;font-size:16px;color:#fff}
.brand i{width:11px;height:11px;border-radius:50%;background:var(--blue);display:block}
.search{left:445px;top:10px;width:159px;height:22px;background:#2a2d32;border:1px solid #34373c}
.search span{position:absolute;left:8px;top:7px;font-size:5.5px;color:#666}
.search .btn{position:absolute;right:0;top:0;width:22px;height:20px;background:var(--blue)}
.nav{left:0;top:62px;width:668px;height:28px;background:var(--blue)}
.nav a{position:absolute;top:0;height:28px;line-height:28px;font-size:6.6px;color:#fff;text-decoration:none;letter-spacing:.2px;transform:translateX(-50%)}
.nav a.home{left:62px;width:42px;transform:none;text-align:center;background:var(--blue-dark)}
.nav a.open{background:var(--blue)}
.hero{left:0;top:90px;width:668px;height:297px;background:linear-gradient(180deg,#3b3f4d 0%,#7a5a52 30%,#d7894a 42%,#5a5b63 55%,#6e7884 72%,#aab3bc 100%)}
.caption{left:250px;top:236px;width:347px;height:84px;background:rgba(40,40,50,.35);color:#fff;text-align:right;padding:10px 16px 0 0;font-family:"Raleway",sans-serif}
.caption h1{font-weight:400;font-size:22px;letter-spacing:.3px;margin-bottom:6px}
.caption p{font-size:7.4px;line-height:15px;letter-spacing:.2px}
.dots{left:318px;top:371px;display:flex;gap:3px}
.dots i{width:6px;height:6px;border-radius:50%;background:rgba(255,255,255,.5);display:block}
.dots i.on{background:var(--blue);border:1px solid #fff}
.dropdown{left:104px;top:90px;width:179px;height:109px;background:rgba(2,70,150,.9);color:#fff;padding:9px 0 0 12px}
.dropdown h4{font-weight:400;font-size:6.4px;margin-bottom:9px}
.dropdown ul{list-style:none;display:grid;grid-template-columns:91px 80px;row-gap:8px;font-size:5.6px}
.dropdown li::before{content:"";display:inline-block;width:0;height:0;border-left:3px solid transparent;border-right:3px solid transparent;border-bottom:5px solid #fff;transform:rotate(45deg);margin:0 4px 0 0}
.strip{left:0;top:387px;width:668px;height:154px;background:var(--strip)}
.arrow{font-size:13px;color:#333;top:453px}
.cat{top:402px;width:126px;height:123px;background:#fff;border:1px solid var(--line);padding:8px}
.cat .ph,.tile .ph{width:109px;display:block}
.cat .ph{height:83px}
.cat h3{font-family:"Raleway",sans-serif;font-weight:500;font-size:8.6px;margin-top:13px;display:flex;justify-content:space-between;align-items:center}
.go{width:8px;height:8px;border-radius:50%;background:var(--blue);display:inline-block;position:relative}
.go::after{content:"";position:absolute;left:2px;top:2.5px;width:2.5px;height:2.5px;border-top:1px solid #fff;border-right:1px solid #fff;transform:rotate(45deg)}
.tile{width:126px;background:#fff;border:1px solid var(--line);padding:8px}
.tile h3{font-family:"Raleway",sans-serif;font-weight:500;font-size:7.8px;margin:14px 0 4px}
.tile p{font-size:5.6px;line-height:11.5px;color:var(--muted)}
.tile .more{display:flex;justify-content:flex-end;align-items:center;gap:3px;font-size:6px;color:var(--blue);margin-top:5px;font-weight:500}
.tile .more .go{width:7px;height:7px}
.loadmore{left:245px;top:1001px;font-size:6.4px;color:var(--blue);font-weight:500}
.side{left:480px;top:562px;width:126px;height:284px;background:var(--panel);padding:9px 10px 0 11px;font-size:6.2px}
.side li{list-style:none}
.side>ul>li{display:flex;justify-content:space-between;align-items:center;height:20px;border-bottom:1px solid #c9ced6}
.side>ul>li.open{display:block;height:69px;padding-top:5px}
.side .row{display:flex;justify-content:space-between}
.side ul ul{margin-top:4px}
.side ul ul li{font-size:5.4px;line-height:11.5px;padding-left:5px;position:relative}
.side ul ul li::before{content:"";position:absolute;left:0;top:4px;border-left:3px solid var(--blue);border-top:2px solid transparent;border-bottom:2px solid transparent}
.pm{width:6px;height:6px;border-radius:50%;background:#555;position:relative;display:inline-block}
.pm::before,.pm.plus::after{content:"";position:absolute;background:#fff}
.pm::before{left:1.5px;top:2.6px;width:3px;height:.8px}
.pm.plus::after{left:2.6px;top:1.5px;width:.8px;height:3px}
.ad{left:480px;width:126px}
.footer{left:0;top:1032px;width:668px;height:128px;background:var(--footer);color:#ddd}
.footer h5{position:absolute;top:24px;font-family:"Raleway",sans-serif;font-weight:500;font-size:8.8px;color:#fff;letter-spacing:.2px}
.news{left:62px;display:flex;gap:5px}
.news .th{width:42px;height:27px;display:block}
.news b{display:block;font-weight:400;font-size:6.2px;color:#fff;margin-bottom:2px}
.news span{font-size:5.6px;color:#999;line-height:8.5px;display:block}
.links{top:1066px;list-style:none;font-size:5.6px;color:#8b8f96;line-height:14.4px}
.field{left:338px;width:120px;height:21px;background:var(--field);font-size:5.4px;color:#777;padding:8px 0 0 10px}
.subscribe{left:338px;top:1120px;width:120px;height:22px;background:var(--blue);color:#fff;font-size:6.4px;text-align:center;line-height:22px}
.bottom{left:0;top:1160px;width:668px;height:40px;background:var(--bottom)}
.bottom p{position:absolute;left:62px;top:17px;font-size:5.6px;color:#666}
.social{position:absolute;left:549px;top:14px;display:flex;gap:3px}
.social i{width:12px;height:12px;display:block;background:var(--blue)}
.social i.red{background:#d6402f}
.social i.sky{background:#2a8fd6}
</style>
</head>
<body>

<div class="abs topbar">
  <ul>
    <li class="call">CALL US : <b>888 - 555 - 0142</b></li>
    <li class="sq">MY ACCOUNT</li>
    <li class="sq">SETTINGS</li>
    <li class="sq">LOGIN</li>
  </ul>
</div>

<div class="abs header"></div>
<div class="abs brand"><i></i>BrambleShore.com</div>
<div class="abs search"><span>Search...</span><div class="btn">
  <svg width="22" height="20" viewBox="0 0 22 20"><circle cx="10.3" cy="9.3" r="2.6" fill="none" stroke="#fff" stroke-width="1.2"/><line x1="12.2" y1="11.2" x2="14" y2="13" stroke="#fff" stroke-width="1.3"/></svg>
</div></div>

<nav class="abs nav">
  <a class="home" href="#">HOME</a>
  <a class="open" style="left:146px" href="#">LODGING</a>
  <a style="left:210px" href="#">DINING</a>
  <a style="left:277px" href="#">WINERIES</a>
  <a style="left:364px" href="#">ACTIVITIES &amp; EVENTS</a>
  <a style="left:458px" href="#">REAL ESTATE</a>
  <a style="left:534px" href="#">FOR SALE</a>
  <a style="left:596px" href="#">JOBS</a>
</nav>

<div class="abs hero" role="img" aria-label="Sunset over a rocky ocean shoreline with waves washing over the rocks"></div>
<div class="abs caption">
  <h1>KAYAK PACKAGE !</h1>
  <p>LOREM IPSUM DOLOR SIT AMET, CONSECTETUER ADIPISCING ELIT, SED<br>DIAM NONUMMY NIBH EUISMOD TINCIDUNT.</p>
</div>
<div class="abs dots"><i class="on"></i><i></i><i></i><i></i></div>

<div class="abs dropdown">
  <h4>GO TO DINING</h4>
  <ul>
    <li>BARS &amp; NIGHTCLUBS</li><li>ITALIAN</li>
    <li>LUNCH &amp; DINNER</li><li>PIZZA</li>
    <li>CATERING</li><li>SEAFOOD</li>
    <li>CHINESE</li><li>STEAKHOUSE</li>
    <li>COFFEE</li><li>MORE</li>
  </ul>
</div>

<div class="abs strip"></div>
<div class="abs arrow" style="left:35px">&#8249;</div>
<div class="abs arrow" style="left:624px">&#8250;</div>
<div class="abs cat" style="left:62px"><span class="ph" role="img" aria-label="Palm trees on a white sand beach" style="background:linear-gradient(180deg,#4d9fe0,#bfe2f5 55%,#e9e2cf)"></span><h3>THE BEACHES <span class="go"></span></h3></div>
<div class="abs cat" style="left:201px"><span class="ph" role="img" aria-label="Wedding bouquet of pink roses" style="background:linear-gradient(160deg,#d9c9c1,#c94f73 45%,#6b7a4f)"></span><h3>WEDDINGS <span class="go"></span></h3></div>
<div class="abs cat" style="left:340px"><span class="ph" role="img" aria-label="Elk standing in a dry grass field" style="background:linear-gradient(180deg,#8a7e6a,#a08c6c 50%,#c7b48e)"></span><h3>WILDLIFE <span class="go"></span></h3></div>
<div class="abs cat" style="left:480px"><span class="ph" role="img" aria-label="Wine bottles, glasses and oak barrels" style="background:linear-gradient(180deg,#3a2a1c,#6b4a2c 50%,#2b1c14)"></span><h3>WINE EVENTS <span class="go"></span></h3></div>

<article class="abs tile" style="left:62px;top:562px;height:185px">
  <span class="ph" role="img" aria-label="Tree-lined park path in autumn" style="height:83px;background:linear-gradient(180deg,#5f7a32,#9a8a3a 60%,#4c3e2a)"></span>
  <h3>BUTTERFLY PARK</h3>
  <p>Lorem ipsum dolor sit amet, consec tetuer adipiscing elit, sed diam nonum my nibh euismod tincidunt ut laoreet dolore magn.</p>
  <div class="more">READ MORE <span class="go"></span></div>
</article>
<article class="abs tile" style="left:62px;top:762px;height:220px">
  <span class="ph" role="img" aria-label="Vineyard hills with a village and church" style="height:107px;background:linear-gradient(180deg,#9fb4c9,#6f8a4e 40%,#c9a84a 80%,#8a6a2a)"></span>
  <h3>PASO ROBLES</h3>
  <p>Ut wisi enim ad minim veniam, quis nostrud exerci tation ullamcorper suscipit lobortis nisl ut aliquip ex ea commodo consequat. Duis autem vel eum iriure dolor in hendrerit.</p>
  <div class="more">READ MORE <span class="go"></span></div>
</article>
<article class="abs tile" style="left:201px;top:562px;height:220px">
  <span class="ph" role="img" aria-label="Mountain valley road under a blue sky" style="height:107px;background:linear-gradient(180deg,#2f7bd0,#a9c7e3 35%,#5b8a3c 65%,#3a5a2a)"></span>
  <h3>SANTA BARBARA</h3>
  <p>Ut wisi enim ad minim veniam, quis nostrud exerci tation ullamcorper suscipit lobortis nisl ut aliquip ex ea commodo consequat. Duis autem vel eum iriure dolor in hendrerit.</p>
  <div class="more">READ MORE <span class="go"></span></div>
</article>
<article class="abs tile" style="left:201px;top:797px;height:185px">
  <span class="ph" role="img" aria-label="Wooden boat on a tropical beach below cliffs" style="height:83px;background:linear-gradient(180deg,#3a78c4,#8ab7d8 40%,#6a7f5a 60%,#d9c7a2)"></span>
  <h3>PISMO BEACH</h3>
  <p>Lorem ipsum dolor sit amet, consec tetuer adipiscing elit, sed diam nonum my nibh euismod tincidunt ut laoreet dolore magn.</p>
  <div class="more">READ MORE <span class="go"></span></div>
</article>
<article class="abs tile" style="left:340px;top:562px;height:198px">
  <span class="ph" role="img" aria-label="Wooden pier on a blue lake with hills" style="height:83px;background:linear-gradient(180deg,#1e62c2,#8fb9e4 40%,#3a6b4a 55%,#1f7fb0)"></span>
  <h3>DINOSAUR CAVES</h3>
  <p>Mirum est notare quam littera gothica, quam nunc putamus parum claram, antep osuerit litterarum formas huma nitatis per seacula quarta decima et quinta decima.</p>
  <div class="more">READ MORE <span class="go"></span></div>
</article>
<article class="abs tile" style="left:340px;top:774px;height:220px">
  <span class="ph" role="img" aria-label="Turquoise mountain lake surrounded by forest" style="height:107px;background:linear-gradient(180deg,#7fa3c4,#4d6a4a 40%,#2fb0a8 70%,#3a6a2a)"></span>
  <h3>MORRO BAY</h3>
  <p>Ut wisi enim ad minim veniam, quis nostrud exerci tation ullamcorper suscipit lobortis nisl ut aliquip ex ea commodo consequat. Duis autem vel eum iriure dolor in hendrerit.</p>
  <div class="more">READ MORE <span class="go"></span></div>
</article>
<div class="abs loadmore">LOAD MORE</div>

<aside class="abs side">
  <ul>
    <li>LODGING <span class="pm plus"></span></li>
    <li class="open"><div class="row">FOOD &amp; WINE <span class="pm"></span></div>
      <ul><li>Wine Tours</li><li>Wineries</li><li>Wine Events</li><li>Dining and Reviews</li></ul>
    </li>
    <li>REAL ESTATE <span class="pm plus"></span></li>
    <li>GOLF <span class="pm plus"></span></li>
    <li>WEDDINGS <span class="pm plus"></span></li>
    <li>ENTERTAINMENT <span class="pm plus"></span></li>
    <li>SERVICES <span class="pm plus"></span></li>
    <li>SHOPPING <span class="pm plus"></span></li>
    <li>FORUMS <span class="pm plus"></span></li>
    <li>CLASSIFIEDS <span class="pm plus"></span></li>
    <li style="border:0">RECREATION <span class="pm plus"></span></li>
  </ul>
</aside>
<div class="abs ad" style="top:856px;height:66px;background:linear-gradient(90deg,#1f6a8a 0%,#4a8fb0 55%,#d9b89a 100%)" role="img" aria-label="Real estate agent advertisement"></div>
<div class="abs ad" style="top:933px;height:75px;background:linear-gradient(180deg,#f4f6fa 0%,#e8edf5 80%,#0d4fa0 80%)" role="img" aria-label="Fernmarsh Inn Pismo Beach lodging and dinner package advertisement"></div>

<footer class="abs footer">
  <h5 style="left:62px">LATEST NEWS</h5>
  <h5 style="left:202px">QUICK LINKS</h5>
  <h5 style="left:338px">NEWSLETTER</h5>
  <h5 style="left:481px">OUR LOCATION</h5>
</footer>
<div class="abs news" style="top:1069px"><span class="th" role="img" aria-label="Beach with palm trees" style="background:linear-gradient(180deg,#3f8fd8,#d8e6d8)"></span><div><b>Lorem ipsum dolor sit</b><span>Ut wisi enim ad minim<br>veniam, quis nostrud...</span></div></div>
<div class="abs news" style="top:1112px"><span class="th" role="img" aria-label="Grapes on the vine" style="background:linear-gradient(180deg,#6e8a3a,#5a3a4a)"></span><div><b>Lorem ipsum dolor sit</b><span>Ut wisi enim ad minim<br>veniam, quis nostrud...</span></div></div>
<ul class="abs links" style="left:202px"><li>Home</li><li>About Us</li><li>Our Service</li><li>FAQ</li><li>Contact Us</li></ul>
<ul class="abs links" style="left:264px"><li>Testimonials</li><li>Privacy Policy</li><li>Sitemap</li><li>Terms &amp; Conditions</li></ul>
<div class="abs field" style="top:1067px">Name</div>
<div class="abs field" style="top:1094px">Email Address</div>
<div class="abs subscribe">SUBSCRIBE</div>
<div class="abs" style="left:481px;top:1070px;width:123px;height:72px;background:linear-gradient(135deg,#e9e4d6,#c9dcc0 50%,#a9c8e4)" role="img" aria-label="Street map showing the office location"></div>
<svg class="abs" style="left:534px;top:1084px" width="14" height="18" viewBox="0 0 14 18"><path d="M7 17C7 17 1 10 1 6.5a6 6 0 0 1 12 0C13 10 7 17 7 17z" fill="#0255a3"/><circle cx="7" cy="6.5" r="2.2" fill="#fff"/></svg>

<div class="abs bottom">
  <p>© 2015 Bramble Shore. All rights reserved</p>
  <div class="social"><i></i><i class="sky"></i><i></i><i class="red"></i></div>
</div>

</body>
</html>
```